Business Card Design Project

QPR Management Consulting, LLC is a management consulting firm focused on improving an organization’s health and wellness while enhancing company performance with an emphasis on winning in the marketplace, profitable growth, team building, culture enablement and innovation.

Industry/Entity Type

Business

```html
<!DOCTYPE html>
<html lang="en">
<head>
<meta charset="utf-8">
<title>QPR Management Consulting – Business Card</title>
<link href="https://fonts.googleapis.com/css2?family=Cinzel:wght@400;600&family=Didact+Gothic&family=Lato:wght@400&family=Marcellus&display=swap" rel="stylesheet">
<style>
  :root {
    --page-bg: #eeeeee;
    --card-bg: #232323;
    --accent: #7dc242;
    --text-light: #f2f2f2;
    --rule: #d9d9d9;
  }
  * { box-sizing: border-box; margin: 0; padding: 0; }
  html, body { width: 1200px; height: 904px; overflow: hidden; background: var(--page-bg); }
  .canvas { position: relative; width: 1200px; height: 904px; }

  .card {
    position: absolute; width: 540px; height: 308px;
    background: var(--card-bg); color: var(--text-light);
    box-shadow: 0 6px 18px rgba(0,0,0,.25); overflow: hidden;
  }

  /* ---------- back card ---------- */
  .card-back { left: 40px; top: 110px; padding: 13px 18px; font-family: "Didact Gothic", sans-serif; font-size: 10.5px; line-height: 1.36; }
  .back-title { font-family: "Cinzel", serif; font-weight: 600; color: var(--accent); font-size: 19px; letter-spacing: .5px; text-align: center; }
  .rule { height: 1px; background: var(--rule); margin: 6px -18px 8px; }
  .label { display: inline-block; background: var(--accent); color: #fff; font-size: 9px; padding: 1px 6px; margin-bottom: 3px; }
  .offerings { display: grid; grid-template-columns: 1fr 1.45fr; column-gap: 10px; }
  .chev-list { list-style: none; white-space: nowrap; }
  .chev-list li::before { content: ">"; color: var(--accent); margin-right: 6px; }
  .numbered { margin-top: 5px; }
  .num { color: var(--accent); margin: 0 3px 0 6px; }
  .num:first-child { margin-left: 0; }
  .values { margin-top: 2px; }
  .values .sep { color: var(--accent); margin: 0 5px; }
  .bullets { list-style: none; margin-top: 3px; }
  .bullets li::before { content: "•"; color: var(--accent); margin-right: 7px; }

  /* ---------- front card ---------- */
  .card-front { left: 620px; top: 486px; }
  .brand-name {
    position: absolute; left: 30px; top: 46px; width: 300px;
    font-family: "Marcellus", serif; font-size: 26px; line-height: 1.15; color: var(--text-light);
  }
  .contact-tab { position: absolute; left: 0; top: 200px; width: 8px; height: 34px; }
  .contact-tab .white { height: 17px; background: #fff; }
  .contact-tab .green { height: 17px; background: var(--accent); }
  .holder { position: absolute; left: 30px; top: 190px; }
  .holder-name { font-family: "Cinzel", serif; color: var(--accent); font-size: 20px; letter-spacing: .5px; }
  .holder-role { font-family: "Lato", sans-serif; font-size: 14px; color: var(--text-light); margin-top: 2px; }
  .contact-list { list-style: none; margin-top: 10px; font-family: "Lato", sans-serif; font-size: 13px; color: var(--text-light); }
  .contact-list li { display: flex; align-items: center; gap: 10px; height: 19px; }
  .contact-list svg { width: 12px; height: 12px; flex: none; }
</style>
</head>
<body>
<div class="canvas">

  <section class="card card-back">
    <h1 class="back-title">QPR MANAGEMENT CONSULTING, LLC</h1>
    <div class="rule"></div>
    <span class="label">SERVICE OFFERINGS:</span>
    <div class="offerings">
      <ul class="chev-list">
        <li>Organizational Health Services</li>
        <li>Company Turnaround Services</li>
        <li>Innovation Lab Establishment</li>
        <li>Enterprise Risk Management</li>
        <li>Business Strategy Development</li>
      </ul>
      <ul class="chev-list">
        <li>Strategic Corporate Communication Strategy Development</li>
        <li>IT Strategy Development</li>
        <li>Complex Program and Project Management</li>
        <li>M&amp;A due diligence support</li>
        <li>Post-M&amp;A Integration Services including:</li>
      </ul>
    </div>
    <p class="numbered">
      <span class="num">1.</span>Change Management <span class="num">2.</span>Organization Design <span class="num">3.</span>Integrated Business Strategy Development<br>
      <span class="num">4.</span>IT Integration Strategy Development <span class="num">5.</span>Leadership Development
    </p>
    <div class="rule"></div>
    <span class="label">Leading with Purpose</span>
    <p class="values"><span class="sep" style="margin-left:0">&gt;</span>Facilitating Change<span class="sep">&gt;</span>Solving Problems<span class="sep">&gt;</span>Building Trust<span class="sep">&gt;</span>Adding Humor<span class="sep">&gt;</span>Bringing Joy</p>
    <ul class="bullets">
      <li>Helping companies achieve change amid order and order amid change</li>
      <li>Helping companies develop a shared consciousness around their business strategies</li>
      <li>Helping companies Dance in the Hurricane</li>
      <li>Helping companies achieve profitable growth</li>
      <li>Enabling companies by effectively leveraging technology and innovation</li>
    </ul>
  </section>

  <section class="card card-front">
    <div class="brand-name">QPR Management Consulting, LLC</div>
    <div class="contact-tab"><div class="white"></div><div class="green"></div></div>
    <div class="holder">
      <div class="holder-name">MARLON TEAGUE</div>
      <div class="holder-role">Director</div>
      <ul class="contact-list">
        <li>
          <svg viewBox="0 0 24 24" aria-hidden="true"><path fill="#7dc242" d="M6.6 10.8a15 15 0 0 0 6.6 6.6l2.2-2.2a1 1 0 0 1 1-.25 11.4 11.4 0 0 0 3.6.57 1 1 0 0 1 1 1V20a1 1 0 0 1-1 1A17 17 0 0 1 3 4a1 1 0 0 1 1-1h3.5a1 1 0 0 1 1 1c0 1.25.2 2.45.57 3.6a1 1 0 0 1-.25 1z"/></svg>
          +1 555 0142 3390
        </li>
        <li>
          <svg viewBox="0 0 24 24" aria-hidden="true"><rect x="2.5" y="5" width="19" height="14" fill="none" stroke="#7dc242" stroke-width="2"/><path d="M3 6l9 7 9-7" fill="none" stroke="#7dc242" stroke-width="2"/></svg>
          hello@qprconsulting.com
        </li>
        <li>
          <svg viewBox="0 0 24 24" aria-hidden="true"><g fill="none" stroke="#7dc242" stroke-width="2"><circle cx="12" cy="12" r="9.5"/><ellipse cx="12" cy="12" rx="4" ry="9.5"/><path d="M2.5 12h19M4 7h16M4 17h16"/></g></svg>
          www.qprconsulting.com
        </li>
      </ul>
    </div>
  </section>

</div>
</body>
</html>
```